Brindlewood Court Apartments Business Cards

We need a business card design for a small apartment community in the metro-Detroit area. The property has a park-like feel and is surrounded by trees and ponds.

The logo colors are:
R=9 G=117 B=127
R=210 G=183 B=114

Contact Information for Business Card

Marla Finch
Property Manager
Brindlewood Court Apartments
352 Brindlewood Way
Cedar Bend, MI 48190
Phone (555)517-2039

```html
<!DOCTYPE html>
<html lang="en">
<head>
<meta charset="utf-8">
<title>Brindlewood Court Apartments – Business Card</title>
<link rel="stylesheet" href="https://fonts.googleapis.com/css2?family=Cinzel:wght@400;700&display=swap">
<style>
  :root {
    --cream: #fcf7d9;
    --cream-deep: #f6efcc;
    --stripe-dark: #b2aa98;
    --stripe-mid: #c9c2ae;
    --stripe-light: #dcd6c2;
    --stripe-faint: rgba(200, 192, 170, 0.28);
    --teal: #09757f;
    --gold: #d2b772;
    --ink: #1f1d1a;
  }
  html, body {
    margin: 0;
    padding: 0;
    overflow: hidden;
    background: #ffffff;
  }
  .card {
    position: relative;
    width: 1200px;
    height: 770px;
    overflow: hidden;
    background: var(--cream);
    font-family: "Cinzel", serif;
  }
  .stripe-panel {
    position: absolute;
    left: 0;
    top: 0;
    width: 497px;
    height: 770px;
  }
  .texture-panel {
    position: absolute;
    left: 497px;
    top: 0;
    width: 703px;
    height: 770px;
    background:
      radial-gradient(ellipse at 30% 35%, rgba(215, 208, 180, 0.45), transparent 55%),
      radial-gradient(ellipse at 80% 70%, rgba(215, 208, 180, 0.35), transparent 55%),
      var(--cream-deep);
  }
  .faint-stripes {
    position: absolute;
    left: 497px;
    top: 0;
    width: 703px;
    height: 770px;
  }
  .brand {
    position: absolute;
    left: 560px;
    top: 60px;
    width: 590px;
    text-align: center;
    color: var(--gold);
    font-weight: 700;
  }
  .brand-mark {
    display: block;
    width: 160px;
    height: 160px;
    margin: 0 auto 58px;
    border-radius: 50%;
    background: var(--gold);
  }
  .brand-name {
    display: block;
    font-size: 44px;
    letter-spacing: 0.06em;
    line-height: 1.1;
    text-transform: uppercase;
    white-space: nowrap;
  }
  .brand-sub {
    display: block;
    font-size: 29px;
    letter-spacing: 0.17em;
    margin-top: 14px;
    text-transform: uppercase;
  }
  .contact {
    position: absolute;
    right: 98px;
    top: 446px;
    text-align: right;
    color: var(--ink);
    font-size: 23px;
    font-weight: 400;
    letter-spacing: 0.2em;
    line-height: 36px;
    text-transform: uppercase;
    margin: 0;
    font-style: normal;
  }
  .contact p { margin: 0; }
  .contact .address { margin-top: 12px; line-height: 33px; }
  .contact .phone { margin-top: 18px; }
</style>
</head>
<body>
  <main class="card">
    <svg class="stripe-panel" viewBox="0 0 497 770" aria-hidden="true">
      <rect x="0" y="0" width="497" height="770" fill="var(--cream)"/>
      <rect x="0" y="0" width="28" height="770" fill="var(--stripe-dark)"/>
      <rect x="47" y="0" width="27" height="770" fill="var(--stripe-dark)"/>
      <rect x="97" y="0" width="27" height="770" fill="var(--stripe-mid)"/>
      <rect x="173" y="0" width="27" height="770" fill="var(--stripe-mid)"/>
      <rect x="290" y="0" width="26" height="770" fill="var(--stripe-light)"/>
    </svg>

    <div class="texture-panel" role="img" aria-label="Faint vine and leaf pattern on a cream background"></div>

    <svg class="faint-stripes" viewBox="0 0 703 770" aria-hidden="true">
      <rect x="48" y="0" width="14" height="770" fill="var(--stripe-faint)"/>
      <rect x="112" y="0" width="8" height="770" fill="var(--stripe-faint)"/>
      <rect x="203" y="0" width="16" height="770" fill="var(--stripe-faint)"/>
      <rect x="310" y="0" width="10" height="770" fill="var(--stripe-faint)"/>
      <rect x="410" y="0" width="18" height="770" fill="var(--stripe-faint)"/>
      <rect x="520" y="0" width="9" height="770" fill="var(--stripe-faint)"/>
      <rect x="610" y="0" width="16" height="770" fill="var(--stripe-faint)"/>
      <rect x="670" y="0" width="10" height="770" fill="var(--stripe-faint)"/>
    </svg>

    <div class="brand">
      <span class="brand-mark" aria-hidden="true"></span>
      <span class="brand-name">Brindlewood Court</span>
      <span class="brand-sub">Apartments</span>
    </div>

    <address class="contact">
      <p class="name">Marla Finch</p>
      <p class="title">Property Manager</p>
      <p class="company">Brindlewood Court Apartments</p>
      <p class="address">352 Brindlewood Way<br>Cedar Bend<br>MI 48190</p>
      <p class="phone">Phone: (555)517-2039</p>
    </address>
  </main>
</body>
</html>
```